Flyer Design for a Boston Therapeutic Clinic

I am a body therapist who needs a couple of flyers designed:
1. To fit half a page.
2. To fit a 5 inch by 3.5 inch flyer.
My practice is based in Boston, MA and my web site is:
www.LarchTessvik.Com
For the First half page:
A. Have my company's name and color shown as it appears on my web site (Larch Tessvik)
B. Have the following text: "Control your weight (This part should be emphasized) by balancing your nervous and digestive system through the Tessvik Method. The Tessvik Method, a technique developed by Dr. Mara. Tessvik, uses physical pressure to manipulate visceral tissue to bring back resiliency and proper functioning of the whole body."
Also helps with
-Constipation
-Bloating
-IBS
-eating disorders and overeating
Our practitioner is highly experienced. Please visit our web sites for reviews.
C. I would like to have a nice earthy feeling, something that feels "freeing" like open flowers, or an open land scape such as mountains or fields.
D. I also like the color blue, white, orange; perhaps if these colors can be integrated into the flyer, that would be great.
E. "Visit our web site LarchTessvik.com or call 786-555-0148"
The Smaller Flyer :
A.The smaller Flyer should also have my Company's name as shown on my web site (Larch Tessvik)
B.The following text: " Restore your body's natural resiliency and greatly reduce your physical pain through the Dr. Mara Tessvik Method of Structural Integration."
C. "Our practitioner is highly experienced and has a great reputation; visit our web site for reviews."
"Benefits:
"reduce aches and pains
reduce joint pain
reduce chronic muscular tension"
D, "feel better after the first session!"
E. if you could use a picture of me working on someone from my web site, that would be great.
F. I also like the colors white, orange and silver, for this one.
G. "Visit our web site LarchTessvik.com or call 786-555 0148"
I am very open minded,
I would like the flyer to evoke a sense of tranquility, professionalism, and simplicity. So if you have another angle you think would look good, then go for it! As long as it looks clean, professional and helpful.
Thanks a lot!
If you need any pictures from my web site, I have the original high resolution files that i can send.
Professionals and working men and women from ages 20-70
Clinic

```html
<!DOCTYPE html>
<html lang="en">
<head>
<meta charset="utf-8">
<title>Larch Tessvik Therapy – Flyers</title>
<link rel="stylesheet" href="https://fonts.googleapis.com/css2?family=Arimo:wght@400;700&family=Oswald:wght@500;700&family=Spectral:wght@400&display=swap">
<style>
  :root {
    --stage: #ece8e2;
    --white: #ffffff;
    --ink: #222222;
    --grey: #6b6b6b;
    --brand: #e2603e;
    --red: #e3262b;
    --red-deep: #c91c20;
    --orange: #e99a35;
    --orange-light: #f0ac4b;
    --orange-accent: #f39b2f;
    --blue: #2e3d8f;
    --beige: #eadfc8;
    --silver: #dcd8d2;
  }
  * { box-sizing: border-box; margin: 0; padding: 0; }
  html, body { width: 1200px; height: 1200px; overflow: hidden; }
  body {
    background: var(--stage);
    font-family: "Arimo", Arial, sans-serif;
    color: var(--ink);
    position: relative;
  }
  .brand-name {
    font-family: "Spectral", Georgia, serif;
    font-weight: 400;
    color: var(--brand);
    white-space: nowrap;
  }

  /* ---------- Small flyer (5 x 3.5) ---------- */
  .small-flyer {
    position: absolute; left: 375px; top: 76px;
    width: 402px; height: 280px;
    background: var(--white);
    box-shadow: 0 3px 8px rgba(0,0,0,.3);
    overflow: hidden;
  }
  .small-flyer .brand-name {
    position: absolute; left: 21px; top: 12px; font-size: 20px;
  }
  .small-flyer .intro {
    position: absolute; left: 21px; top: 54px; width: 245px;
    font-size: 9px; line-height: 13px;
  }
  .small-flyer .practice-photo {
    position: absolute; left: 277px; top: 0; width: 125px; height: 150px;
    background: radial-gradient(circle at 40% 55%, #c47a4c 0%, #8a3f1f 45%, #3a1a0f 100%);
  }
  .small-flyer .reputation {
    position: absolute; left: 0; top: 117px; width: 277px; height: 33px;
    background: linear-gradient(180deg, var(--beige), #f5efe2);
    padding: 6px 21px 0; font-size: 8px; line-height: 11px;
  }
  .small-flyer .reputation b { font-weight: 700; }
  .small-flyer .contact-strip {
    position: absolute; left: 0; top: 150px; width: 402px; height: 34px;
    background: linear-gradient(180deg, #f6f3ee, var(--silver));
    padding: 13px 21px 0; font-size: 11px;
  }
  .small-flyer .contact-strip b { font-weight: 700; font-size: 12px; }
  .small-flyer .benefits {
    position: absolute; left: 0; top: 184px; width: 402px; height: 96px;
    background: linear-gradient(180deg, var(--red), var(--red-deep));
    color: var(--white);
  }
  .small-flyer .benefits h2 {
    position: absolute; left: 21px; top: 10px;
    font-family: "Arimo", Arial, sans-serif; font-weight: 400; font-size: 17px;
  }
  .small-flyer .benefits ul {
    position: absolute; left: 21px; top: 37px; list-style: none;
    font-size: 10px; font-weight: 700; line-height: 16px;
  }
  .small-flyer .benefits li::before {
    content: ""; display: inline-block; width: 6px; height: 6px;
    border-radius: 50%; background: var(--white); margin-right: 9px;
  }
  .small-flyer .first-session {
    position: absolute; left: 250px; top: 17px; width: 140px;
    font-family: "Oswald", Impact, sans-serif; font-weight: 700;
    font-size: 17px; line-height: 23px; text-align: center;
    text-shadow: 1px 1px 2px rgba(0,0,0,.4);
  }

  /* ---------- Half page flyer ---------- */
  .half-flyer {
    position: absolute; left: 129px; top: 433px;
    width: 938px; height: 663px;
    background: linear-gradient(160deg, var(--orange-light), var(--orange) 60%, #e08f2c);
    box-shadow: 0 4px 10px rgba(0,0,0,.35);
    overflow: hidden;
    color: var(--ink);
  }
  .half-flyer .header-bands { position: absolute; left: 0; top: 0; }
  .half-flyer .brand-name {
    position: absolute; left: 38px; top: 47px; font-size: 37px;
  }
  .half-flyer .call {
    position: absolute; left: 600px; top: 38px; width: 330px; color: var(--white);
    font-family: "Arimo", Arial, sans-serif; font-size: 26px; white-space: nowrap;
  }
  .half-flyer .call b {
    font-family: "Oswald", Impact, sans-serif; font-weight: 700; font-size: 40px;
    vertical-align: -3px; margin-left: 4px;
  }
  .half-flyer .lead {
    position: absolute; left: 44px; top: 146px; width: 584px;
    font-size: 20.5px; line-height: 35px; text-align: justify;
  }
  .half-flyer .helps-title {
    position: absolute; left: 44px; top: 408px;
    font-size: 25px; font-weight: 400; color: var(--white);
  }
  .half-flyer .helps-list {
    position: absolute; left: 44px; top: 448px; width: 500px;
    list-style: none; display: grid; grid-template-columns: 173px auto;
    row-gap: 4px; font-size: 19px;
  }
  .half-flyer .helps-list li::before {
    content: ""; display: inline-block; width: 9px; height: 9px;
    background: var(--red); margin-right: 20px; vertical-align: 2px;
  }
  .half-flyer .reviews {
    position: absolute; left: 44px; top: 511px; width: 584px;
    font-size: 17.5px; line-height: 23px;
  }
  .half-flyer .website {
    position: absolute; left: 47px; top: 590px; color: var(--white);
    font-size: 23px; white-space: nowrap;
  }
  .half-flyer .website span { font-size: 34px; }
  .half-flyer .anatomy {
    position: absolute; left: 676px; width: 219px;
    box-shadow: 0 3px 6px rgba(0,0,0,.4);
  }
  .half-flyer .anatomy.shoulder { top: 155px; height: 129px;
    background: radial-gradient(ellipse at 45% 45%, #d9cdb6 0%, #7d725f 35%, #141210 75%); }
  .half-flyer .anatomy.chest { top: 309px; height: 138px;
    background: radial-gradient(ellipse at 50% 50%, #e4dccb 0%, #8f8573 45%, #2a2620 100%); }
  .half-flyer .anatomy.back { top: 473px; height: 143px;
    background: radial-gradient(ellipse at 50% 60%, #e5c98f 0%, #8a7350 35%, #0f0d0a 75%); }
  .half-flyer .footer-band {
    position: absolute; left: 0; bottom: 0; width: 938px; height: 23px;
    background: var(--blue);
  }
</style>
</head>
<body>

<section class="small-flyer" aria-label="Small flyer">
  <div class="brand-name">Larch Tessvik Therapy</div>
  <p class="intro">Restore your body's natural resiliency and greatly reduce your physical pain through the Dr. Mara Tessvik Method of Structural Integration.</p>
  <div class="practice-photo" role="img" aria-label="Photo of the practitioner working on a client's shoulder"></div>
  <p class="reputation"><b>Our practitioner is highly experienced and has a great reputation;</b> VISIT OUR WEB SITE FOR REVIEWS.</p>
  <p class="contact-strip">Visit our web site <b>LarchTessvik.com</b> or call <b>786-555 0148</b></p>
  <div class="benefits">
    <h2>Benefits</h2>
    <ul>
      <li>Reduce aches and pains</li>
      <li>Reduce joint pain</li>
      <li>Reduce chronic muscular tension</li>
    </ul>
    <p class="first-session">Feel better after the First Session!</p>
  </div>
</section>

<section class="half-flyer" aria-label="Half page flyer">
  <svg class="header-bands" width="938" height="110" viewBox="0 0 938 110" aria-hidden="true">
    <polygon points="0,20 540,20 552,40 0,40" fill="var(--blue)"/>
    <polygon points="0,40 552,40 560,104 0,104" fill="var(--white)"/>
    <polygon points="505,0 560,0 600,104 560,104 530,20" fill="var(--orange-accent)"/>
    <polygon points="531,0 938,0 938,104 575,104" fill="var(--red)"/>
  </svg>
  <div class="brand-name">Larch Tessvik Therapy</div>
  <div class="call">Call <b>786-555-0148</b></div>

  <p class="lead">Control your weight (This part should be emphasized) by balancing your nervous and digestive system through the Tessvik Method. The Tessvik Method, a technique developed by Dr. Mara. Tessvik, uses physical pressure to manipulate visceral tissue to bring back resiliency and proper functioning of the whole body.</p>

  <h2 class="helps-title">Also helps with</h2>
  <ul class="helps-list">
    <li>Constipation</li>
    <li>Bloating</li>
    <li>IBS</li>
    <li>Eating disorders and overeating</li>
  </ul>
  <p class="reviews">Our practitioner is highly experienced. Please visit our web sites for reviews.</p>
  <p class="website">Visit our web site <span>LarchTessvik.com</span></p>

  <div class="anatomy shoulder" role="img" aria-label="Anatomical render of a shoulder and ribcage"></div>
  <div class="anatomy chest" role="img" aria-label="Anatomical render of a chest skeleton and shoulder joint"></div>
  <div class="anatomy back" role="img" aria-label="Anatomical render of a back with glowing spine"></div>
  <div class="footer-band"></div>
</section>

</body>
</html>
```